Outdoor Company Business Card design

We are an outdoor adventure company needing a business card. We sell outdoor adventures and clothing. Please use our logo in the business card. We are looking for something unique but delivers a clear message as to who we are. Please be creative

Target Market(s)

Outdoor adventures

Industry/Entity Type

Business

Contact Information for Business Card

Business name: TrailBirch If using the logo, no need to have a spot for the name
Owner / CEO: Ross Dalby
Website: TrailBirch.example
Facebook: Facebook.com/TrailBirch
Instagram: @dalby_ross
phone number: 555-304-7192
Email: Dalbycrew@TrailBirch.example

Colors

Designer to choose colors to be used in the design.

Requirements
Must have
• The business card must include the details mentioned above. ie logo, my name, email, facebook, instagram, website, and phone number.
Should not have
• should not be cluttered or look messy

```html
<!DOCTYPE html>
<html lang="en">
<head>
<meta charset="utf-8">
<title>TrailBirch Business Card</title>
<link rel="stylesheet" href="https://fonts.googleapis.com/css2?family=Open+Sans:wght@400;600;700&display=swap">
<style>
  :root {
    --ink-blue: #0d5096;
    --bright-blue: #1f74c4;
    --trail-orange: #f05a22;
    --paper: #ffffff;
    --muted: #7a7a7a;
    --backdrop: #e6e8eb;
  }
  * { margin: 0; padding: 0; box-sizing: border-box; }
  html, body {
    width: 1200px; height: 900px; overflow: hidden;
    background: var(--backdrop);
    font-family: "Open Sans", sans-serif;
  }
  .sheet {
    position: relative; width: 1200px; height: 900px;
    display: flex; align-items: center; justify-content: center; gap: 54px;
  }
  .card {
    position: relative; width: 520px; height: 300px;
    border-radius: 22px; overflow: hidden; background: var(--paper);
    box-shadow: 0 10px 24px rgba(0,0,0,.18);
  }
  .card-art { position: absolute; inset: 0; width: 100%; height: 100%; }
  .card-art .blue-field { fill: var(--ink-blue); }
  .card-art .orange-swoosh { fill: var(--trail-orange); }

  /* front */
  .front-brand {
    position: absolute; left: 40px; top: 92px;
    color: var(--paper); font-weight: 700; font-size: 27px; letter-spacing: 1px;
  }
  .contact-block {
    position: absolute; right: 36px; top: 58px; width: 290px; text-align: right;
  }
  .person-name { color: var(--ink-blue); font-weight: 700; font-size: 30px; line-height: 1.1; }
  .person-role { color: var(--muted); font-size: 17px; margin-top: 2px; }
  .divider { height: 1px; background: var(--bright-blue); margin: 12px 0 12px; }
  .contact-line {
    display: flex; justify-content: flex-end; align-items: center; gap: 8px;
    color: #444; font-size: 14px; line-height: 1.75;
  }
  .contact-line svg { width: 13px; height: 13px; fill: var(--trail-orange); flex: none; }

  /* back */
  .back-brand {
    position: absolute; left: 0; right: 0; top: 62px; text-align: center;
    color: var(--bright-blue); font-weight: 700; font-size: 38px; letter-spacing: 1.5px;
  }
  .social-handle { fill: #888; font-size: 12px; }
  .social-dot { fill: var(--trail-orange); }
  .web-address { fill: var(--paper); font-size: 14px; font-weight: 600; }
</style>
</head>
<body>
<main class="sheet">

  <section class="card card-front" aria-label="Card front">
    <svg class="card-art" viewBox="0 0 520 300" aria-hidden="true">
      <path class="blue-field" d="M0 0 H300 C245 110 175 210 145 300 H0 Z"/>
      <path class="orange-swoosh" d="M300 0 H318 C262 110 190 210 162 300 H145 C175 210 245 110 300 0 Z"/>
      <path class="orange-swoosh" d="M318 0 H322 C280 80 230 150 190 200 C225 140 275 70 318 0 Z"/>
    </svg>
    <div class="front-brand">TRAILBIRCH</div>
    <div class="contact-block">
      <div class="person-name">Ross Dalby</div>
      <div class="person-role">Owner / CEO</div>
      <div class="divider"></div>
      <div class="contact-line">555-304-7192
        <svg viewBox="0 0 24 24"><path d="M6.6 10.8a15 15 0 0 0 6.6 6.6l2.2-2.2a1 1 0 0 1 1-.25 11.4 11.4 0 0 0 3.6.57 1 1 0 0 1 1 1V20a1 1 0 0 1-1 1A17 17 0 0 1 3 4a1 1 0 0 1 1-1h3.5a1 1 0 0 1 1 1c0 1.25.2 2.45.57 3.57a1 1 0 0 1-.25 1z"/></svg>
      </div>
      <div class="contact-line">Dalbycrew@trailbirch.example
        <svg viewBox="0 0 24 24"><path d="M2 5h20v14H2z M2 5l10 8 10-8" stroke="#fff" stroke-width="1.5"/></svg>
      </div>
      <div class="contact-line">www.trailbirch.example
        <svg viewBox="0 0 24 24"><circle cx="12" cy="12" r="10"/><path d="M2 12h20M12 2c3 3 3 17 0 20M12 2c-3 3-3 17 0 20" stroke="#fff" stroke-width="1.3" fill="none"/></svg>
      </div>
    </div>
  </section>

  <section class="card card-back" aria-label="Card back">
    <svg class="card-art" viewBox="0 0 520 300">
      <path class="blue-field" d="M0 110 C170 170 360 255 520 282 V300 H0 Z"/>
      <path class="orange-swoosh" d="M0 88 H12 C180 160 370 240 520 262 V282 C360 255 170 170 0 110 Z"/>
      <path class="orange-swoosh" d="M70 150 C200 200 330 245 440 262 C320 252 190 210 70 150 Z" fill="#fff" opacity=".0"/>
      <g transform="rotate(17 150 150)">
        <rect class="social-dot" x="104" y="135" width="9" height="9" rx="2"/>
        <text class="social-handle" x="118" y="144">TrailBirch</text>
        <circle class="social-dot" cx="205" cy="140" r="4.5"/>
        <text class="social-handle" x="214" y="144">dalby_ross</text>
      </g>
      <text class="web-address" x="120" y="200" transform="rotate(20 120 200)">www.trailbirch.example</text>
    </svg>
    <div class="back-brand">TRAILBIRCH</div>
  </section>

</main>
</body>
</html>
```